BRWSN Energy Drink - Custom Label

We are looking to design a label for an energy drink with a theme of harbor folly.

This will be an energy drink we give out to customers.

One idea for a name is "BRWSN Bramble Surge"

Decal. 4.65" W x 1.81" H on bottle Barrel Wrap. Full Color Decal, Full Wrap

Target Market(s)

Cannabis

Industry/Entity Type

Cannabis

Requirements
Must have
• BRWSN Logo

```html
<!DOCTYPE html>
<html lang="en">
<head>
<meta charset="UTF-8">
<title>BRWSN Bramble Surge – Energy Drink Label</title>
<link href="https://fonts.googleapis.com/css2?family=Rye&family=Cabin+Sketch:wght@400;700&family=Montserrat:wght@400;800&display=swap" rel="stylesheet">
<style>
  :root {
    --page: #e7e9eb;
    --slate-dark: #3f3f3c;
    --slate-mid: #5b5b56;
    --slate-light: #77766f;
    --lime: #6dbb3a;
    --lime-soft: rgba(109, 187, 58, 0.55);
    --chalk: #f1f1ee;
    --brand-blue: #2a4f80;
  }
  * { margin: 0; padding: 0; box-sizing: border-box; }
  html, body {
    width: 1200px;
    height: 1200px;
    overflow: hidden;
    background: var(--page);
  }
  .canvas {
    position: relative;
    width: 1200px;
    height: 1200px;
  }
  .label {
    position: absolute;
    left: 250px;
    top: 147px;
    width: 700px;
    height: 906px;
    overflow: hidden;
    text-align: center;
  }
  .label-art {
    position: absolute;
    inset: 0;
    background:
      radial-gradient(circle at 0% 8%, var(--lime-soft) 0, rgba(109,187,58,0.15) 22%, transparent 38%),
      radial-gradient(circle at 100% 92%, var(--lime-soft) 0, rgba(109,187,58,0.15) 22%, transparent 38%),
      radial-gradient(ellipse at 50% 45%, var(--slate-light) 0, var(--slate-mid) 45%, var(--slate-dark) 100%);
  }
  .label-content {
    position: relative;
    z-index: 1;
    height: 100%;
  }
  .brand-mark {
    position: absolute;
    top: 205px;
    left: 0;
    right: 0;
    display: flex;
    justify-content: center;
    align-items: center;
    gap: 12px;
    font-family: "Montserrat", sans-serif;
    font-weight: 800;
    font-size: 50px;
    letter-spacing: 1px;
    color: var(--brand-blue);
  }
  .brand-dot {
    width: 16px;
    height: 16px;
    border-radius: 50%;
    background: var(--brand-blue);
  }
  .product-kicker {
    position: absolute;
    top: 318px;
    left: 0;
    right: 0;
    font-family: "Rye", serif;
    font-size: 64px;
    color: var(--chalk);
    letter-spacing: 1px;
  }
  .product-name {
    position: absolute;
    top: 385px;
    left: 0;
    right: 0;
    font-family: "Rye", serif;
    font-size: 178px;
    line-height: 1.2;
    color: var(--lime);
  }
  .product-type {
    position: absolute;
    top: 660px;
    left: 0;
    right: 0;
    font-family: "Cabin Sketch", cursive;
    font-size: 44px;
    line-height: 1.05;
    letter-spacing: 5px;
    color: var(--chalk);
  }
  .product-note {
    position: absolute;
    top: 790px;
    left: 0;
    right: 0;
    font-family: "Montserrat", sans-serif;
    font-size: 15px;
    line-height: 1.4;
    color: var(--chalk);
  }
</style>
</head>
<body>
  <main class="canvas">
    <section class="label">
      <div class="label-art" role="img" aria-label="Distressed charcoal grunge texture with lime halftone swirls in the top-left and bottom-right corners"></div>
      <div class="label-content">
        <div class="brand-mark"><span class="brand-dot"></span>BRWSN</div>
        <h2 class="product-kicker">BRAMBLE</h2>
        <h1 class="product-name">SURGE</h1>
        <p class="product-type">ENERGY<br>DRINK</p>
        <p class="product-note">Lorem ipsum dolor sit amet, consectetur adipiscing elit,<br>sed do eiusmod tempor incididunt ut labore.</p>
      </div>
    </section>
  </main>
</body>
</html>
```